Desing for real estate offers- Package system

The word should be graphically clear and understandable. There are 3 packages that the customer can buy: the basic package is red, the medicinal package is green and the carefree package is blue. See the Word document in the appendix. End file should be a Word, as we need to chance the text. It should also match the website as well as the business card.
https://brelvona.domistra.ch/
Colors:
Green 1: R: 187, G: 214, B: 49
Green 2: R: 119, G: 187, W: 66

Target Market(s)

Real estate company

Font styles to use
Serif
Sans Serif

```html
<!DOCTYPE html>
<html lang="de">
<head>
<meta charset="utf-8">
<title>Brelvona – Individuelle Vermarktungspakete</title>
<link rel="stylesheet" href="https://fonts.googleapis.com/css2?family=Open+Sans:wght@400;600;700;800&display=swap">
<style>
  :root{
    --green-light:#bbd631;
    --green:#77bb42;
    --row-a:#e4efd7;
    --row-b:#d2e3bb;
    --price-bg:#f1f1f1;
    --text-grey:#555555;
    --ink:#111111;
    --tick:#5f9a3a;
    --cross:#d9473d;
  }
  *{box-sizing:border-box;margin:0;padding:0}
  html,body{width:848px;height:1200px;overflow:hidden;background:#fff}
  body{font-family:"Open Sans",Verdana,sans-serif;position:relative;color:var(--ink)}

  .brand{position:absolute;left:53px;top:38px;display:flex;align-items:center;gap:10px}
  .brand-mark{width:12px;height:12px;background:var(--text-grey)}
  .brand-name{font-size:28px;font-weight:700;color:var(--text-grey);line-height:1}

  .edge-band{position:absolute;right:0;top:0;width:17px;height:107px;background:var(--green-light)}

  .contact{position:absolute;right:30px;top:40px;text-align:right;font-size:12px;font-weight:600;line-height:16px}
  .contact .phone{display:inline-flex;align-items:center;gap:4px}
  .contact svg{width:12px;height:12px}

  .title{position:absolute;left:0;width:848px;top:168px;text-align:center;font-size:19px;font-weight:700;color:var(--text-grey);letter-spacing:.3px}

  .intro{position:absolute;left:71px;width:706px;top:236px;font-size:14.5px;line-height:21px;text-align:justify;text-align-last:left}

  .packages{position:absolute;left:43px;top:289px;display:grid;
    grid-template-columns:213px 178px 167px 179px;column-gap:4px;row-gap:2px;
    grid-template-rows:27px 71px repeat(22,33px)}
  .corner{grid-row:1 / span 2;background:var(--price-bg)}
  .pkg-name{background:var(--green);color:#fff;font-weight:800;font-size:18px;display:flex;align-items:center;justify-content:center;letter-spacing:.3px;border-top:3px solid var(--green-light)}
  .pkg-price{background:var(--price-bg);display:flex;flex-direction:column;align-items:center;justify-content:center;color:var(--text-grey);text-align:center;line-height:1.1}
  .pkg-price .amount{font-size:14px;font-weight:700}
  .pkg-price .amount b{font-size:17px}
  .pkg-price .vat{font-size:9.5px;font-weight:700}
  .pkg-price .pct{font-size:15px;font-weight:700}
  .service{background:var(--green);color:#fff;font-size:10.5px;font-weight:700;display:flex;align-items:center;justify-content:center;text-align:center;line-height:11px;padding:0 20px}
  .cell{display:flex;align-items:center;justify-content:center}
  .cell svg{width:16px;height:16px}
  .odd{background:var(--row-a)}
  .even{background:var(--row-b)}
</style>
</head>
<body>
<svg width="0" height="0" style="position:absolute">
  <defs>
    <symbol id="tick" viewBox="0 0 16 16"><path d="M2 8.5l4 4L14 3" fill="none" stroke="var(--tick)" stroke-width="2.2" stroke-linecap="round" stroke-linejoin="round"/></symbol>
    <symbol id="cross" viewBox="0 0 16 16"><path d="M3.5 3.5l9 9M12.5 3.5l-9 9" fill="none" stroke="var(--cross)" stroke-width="2.2" stroke-linecap="round"/></symbol>
  </defs>
</svg>

<header>
  <div class="brand"><span class="brand-mark"></span><span class="brand-name">Brelvona</span></div>
  <div class="edge-band"></div>
  <div class="contact">
    <span class="phone"><svg viewBox="0 0 24 24"><path d="M6.6 10.8a15.1 15.1 0 006.6 6.6l2.2-2.2a1 1 0 011-.25 11.4 11.4 0 003.6.57 1 1 0 011 1V20a1 1 0 01-1 1A17 17 0 013 4a1 1 0 011-1h3.5a1 1 0 011 1 11.4 11.4 0 00.57 3.6 1 1 0 01-.25 1z" fill="#111"/></svg>+41445123456</span><br>
    info@brelvona.ch<br>
    www.brelvona.ch
  </div>
</header>

<h1 class="title">INDIVIDUELLE VERMARKTUNGSPAKETE</h1>

<p class="intro">Unterlagen müssen gestellt werden, ansonsten werden Sie 1:1 verrechnet: GB-Auszug,GVZ, Nebenkostenabrechnung, STWEG-Protokolle der letzten 3 Jahren, …</p>

<section class="packages">
  <div class="corner"></div>
  <div class="pkg-name">BASIS PAKET</div>
  <div class="pkg-name">MEDIUM PAKET</div>
  <div class="pkg-name">SORGLOS</div>
  <div class="pkg-price"><span class="amount">CHF <b>8'500</b></span><span class="vat">exkl. MWST</span></div>
  <div class="pkg-price"><span class="amount">CHF <b>10'900</b></span><span class="vat">exkl. MWST</span></div>
  <div class="pkg-price"><span class="pct">2% vom<br>Verkaufspreis</span><span class="vat">inkl. MWST (von<br>Grundstückgewinnsteuer<br>abziehbar)</span></div>

  <div class="service">Begehung Verkaufsobjekt</div><div class="cell odd"><svg><use href="#tick"/></svg></div><div class="cell odd"><svg><use href="#tick"/></svg></div><div class="cell odd"><svg><use href="#tick"/></svg></div>
  <div class="service">Hedonische Schätzung intern &amp; Bank</div><div class="cell even"><svg><use href="#tick"/></svg></div><div class="cell even"><svg><use href="#tick"/></svg></div><div class="cell even"><svg><use href="#tick"/></svg></div>
  <div class="service">Marketing &amp; Vertriebskonzept</div><div class="cell odd"><svg><use href="#tick"/></svg></div><div class="cell odd"><svg><use href="#tick"/></svg></div><div class="cell odd"><svg><use href="#tick"/></svg></div>
  <div class="service">Unterlagen einfordern- STWEG Protokolle, GB Auszug u.s.w wenn nötig</div><div class="cell even"><svg><use href="#tick"/></svg></div><div class="cell even"><svg><use href="#tick"/></svg></div><div class="cell even"><svg><use href="#tick"/></svg></div>
  <div class="service">Fotografieren &amp; Ausmessen der Immobilie</div><div class="cell odd"><svg><use href="#tick"/></svg></div><div class="cell odd"><svg><use href="#tick"/></svg></div><div class="cell odd"><svg><use href="#tick"/></svg></div>
  <div class="service">Grundriss zeichnen</div><div class="cell even"><svg><use href="#tick"/></svg></div><div class="cell even"><svg><use href="#tick"/></svg></div><div class="cell even"><svg><use href="#tick"/></svg></div>
  <div class="service">Dokumentation erstellen</div><div class="cell odd"><svg><use href="#tick"/></svg></div><div class="cell odd"><svg><use href="#tick"/></svg></div><div class="cell odd"><svg><use href="#tick"/></svg></div>
  <div class="service">Unsere Interessenten anschreiben</div><div class="cell even"><svg><use href="#cross"/></svg></div><div class="cell even"><svg><use href="#tick"/></svg></div><div class="cell even"><svg><use href="#tick"/></svg></div>
  <div class="service">Immobilie Online aufbereiten &amp; Aufschalten</div><div class="cell odd"><svg><use href="#tick"/></svg></div><div class="cell odd"><svg><use href="#tick"/></svg></div><div class="cell odd"><svg><use href="#tick"/></svg></div>
  <div class="service">Anfragen beantworten- telefonisch &amp; elektronisch</div><div class="cell even"><svg><use href="#cross"/></svg></div><div class="cell even"><svg><use href="#tick"/></svg></div><div class="cell even"><svg><use href="#tick"/></svg></div>
  <div class="service">Besichtigungen koordinieren</div><div class="cell odd"><svg><use href="#cross"/></svg></div><div class="cell odd"><svg><use href="#cross"/></svg></div><div class="cell odd"><svg><use href="#tick"/></svg></div>
  <div class="service">Besichtigungen Durchführen</div><div class="cell even"><svg><use href="#cross"/></svg></div><div class="cell even"><svg><use href="#cross"/></svg></div><div class="cell even"><svg><use href="#tick"/></svg></div>
  <div class="service">Interessenten &amp; Kaufangebote prüfen</div><div class="cell odd"><svg><use href="#tick"/></svg></div><div class="cell odd"><svg><use href="#tick"/></svg></div><div class="cell odd"><svg><use href="#tick"/></svg></div>
  <div class="service">Evt. Bieterverfahren modern oder altmodisch</div><div class="cell even"><svg><use href="#cross"/></svg></div><div class="cell even"><svg><use href="#tick"/></svg></div><div class="cell even"><svg><use href="#tick"/></svg></div>
  <div class="service">Käufer zusage- andere noch vertrösten</div><div class="cell odd"><svg><use href="#cross"/></svg></div><div class="cell odd"><svg><use href="#cross"/></svg></div><div class="cell odd"><svg><use href="#tick"/></svg></div>
  <div class="service">Sicherheitsnachweis (SINA)- organisieren</div><div class="cell even"><svg><use href="#cross"/></svg></div><div class="cell even"><svg><use href="#cross"/></svg></div><div class="cell even"><svg><use href="#tick"/></svg></div>
  <div class="service">Erstellung erster Kaufvertragsentwurf</div><div class="cell odd"><svg><use href="#tick"/></svg></div><div class="cell odd"><svg><use href="#tick"/></svg></div><div class="cell odd"><svg><use href="#tick"/></svg></div>
  <div class="service">Berechnung provisorische Grundstückgewinnsteuer-Steueramt</div><div class="cell even"><svg><use href="#cross"/></svg></div><div class="cell even"><svg><use href="#cross"/></svg></div><div class="cell even"><svg><use href="#tick"/></svg></div>
  <div class="service">Beurkundungstermin vereinbaren</div><div class="cell odd"><svg><use href="#cross"/></svg></div><div class="cell odd"><svg><use href="#cross"/></svg></div><div class="cell odd"><svg><use href="#tick"/></svg></div>
  <div class="service">Begleitung aufs Notariat</div><div class="cell even"><svg><use href="#cross"/></svg></div><div class="cell even"><svg><use href="#tick"/></svg></div><div class="cell even"><svg><use href="#tick"/></svg></div>
  <div class="service">Eigentumsübertragung vereinbaren</div><div class="cell odd"><svg><use href="#cross"/></svg></div><div class="cell odd"><svg><use href="#cross"/></svg></div><div class="cell odd"><svg><use href="#tick"/></svg></div>
  <div class="service">Helfen bei der Steuererklärung für die definitive Grundstückgewinnsteuer</div><div class="cell even"><svg><use href="#cross"/></svg></div><div class="cell even"><svg><use href="#cross"/></svg></div><div class="cell even"><svg><use href="#tick"/></svg></div>
</section>
</body>
</html>
```